DJ Competition Audition Flyer

We are looking for an updated version of last years campaign design. See attached image which captures the style and feel for our target market audience ranging from 18-35 years.
Please leave out any dates and just focus on the title'Velvet Tideline DJ Competition, images, general theme/design.
Eye candy, WOW factor,
Words like BLAZE FM, COMPETITION, DJ and PRIZES should be the main focus
Thanks!
Target Market(s)
18-35 years DJ';s and Electronic Music Producers
Industry/Entity Type
Music Training
Colors
Designer to choose colors to be used in the design.
Requirements
Must have
- Website address, contact number,
- Eye candy, WOW factor,
- Words like BLAZE FM, COMPETITION, DJ and PRIZES should be the main focus
Should not have
- Any dates

```html
<!DOCTYPE html>
<html lang="en">
<head>
<meta charset="utf-8">
<title>Velvet Tideline DJ Competition</title>
<link href="https://fonts.googleapis.com/css2?family=Bebas+Neue&family=Oswald:wght@300;400;500&family=Arimo:wght@400;700&display=swap" rel="stylesheet">
<style>
  :root {
    --night: #140a38;
    --indigo: #2a1a78;
    --violet: #6a2bd0;
    --magenta: #a62fd6;
    --cyan: #7ff4ff;
    --coral: #ff6a78;
    --white: #ffffff;
    --diamond-fill: #151035;
  }
  * { margin: 0; padding: 0; box-sizing: border-box; }
  html, body { width: 914px; height: 1200px; overflow: hidden; background: var(--night); }
  .flyer {
    position: relative; width: 914px; height: 1200px; overflow: hidden; color: var(--white);
    background:
      radial-gradient(ellipse 260px 200px at 0px 640px, rgba(255,106,120,.85), transparent 70%),
      radial-gradient(ellipse 520px 180px at 460px 230px, rgba(127,244,255,.55), transparent 70%),
      radial-gradient(ellipse 420px 300px at 560px 900px, rgba(166,47,214,.75), transparent 70%),
      linear-gradient(180deg, #2b1466 0%, #3a2aa0 22%, #5a3ad8 40%, #6a2bd0 60%, #4a1a9a 78%, #1a0c44 100%);
  }
  .beams { position: absolute; inset: 0; }
  .stage-scene { position: absolute; left: 0; top: 760px; width: 914px; height: 440px;
    background: linear-gradient(180deg, transparent, rgba(40,10,90,.55)); }
  .headline { position: absolute; width: 100%; text-align: center; }
  .event-name { top: 22px; font-family: "Oswald", sans-serif; font-weight: 300; font-size: 56px; letter-spacing: -1px; line-height: 1; }
  .event-title { top: 92px; font-family: "Bebas Neue", sans-serif; font-size: 124px; line-height: 1; letter-spacing: 1px; }
  .prizes-label { position: absolute; left: 297px; top: 395px; width: 310px; text-align: center;
    font-family: "Oswald", sans-serif; font-weight: 300; font-size: 34px; letter-spacing: 6px; line-height: 42px; }
  .prize-list { position: absolute; left: 150px; top: 466px; width: 612px; list-style: none; text-align: center;
    font-family: "Arimo", sans-serif; font-size: 22px; line-height: 33px; }
  .prize-list .station { font-weight: 700; font-size: 24px; letter-spacing: 0.5px; }
  .school-name { position: absolute; left: 286px; top: 680px; width: 340px; text-align: center; white-space: nowrap;
    font-family: "Arimo", sans-serif; font-weight: 700; font-size: 15px; letter-spacing: 0.5px; }
  .school-name .dot { display: inline-block; width: 10px; height: 10px; border-radius: 50%; background: var(--white); margin-right: 7px; vertical-align: 0; }
  .presenter { position: absolute; right: 89px; top: 738px; text-align: right; line-height: 1; }
  .presenter .short { font-family: "Arimo", sans-serif; font-weight: 700; font-size: 52px; display: block; }
  .presenter .verb { font-family: "Oswald", sans-serif; font-weight: 400; font-size: 30px; }
  .judges { position: absolute; top: 920px; width: 100%; text-align: center;
    font-family: "Oswald", sans-serif; font-weight: 300; font-size: 32px; letter-spacing: -0.5px; }
  .judges .sep { margin: 0 12px; }
  .cta { position: absolute; left: 94px; top: 981px; width: 722px; height: 77px; border: 1.5px solid var(--white);
    text-align: center; font-family: "Bebas Neue", sans-serif; font-size: 72px; letter-spacing: 5px; line-height: 82px; background: rgba(20,10,56,.35); }
  .contact { position: absolute; width: 100%; text-align: center; font-family: "Oswald", sans-serif; font-weight: 500; }
  .contact-label { top: 1090px; font-size: 14px; letter-spacing: 3px; }
  .contact-main { top: 1114px; font-size: 21px; letter-spacing: 1px; }
  .contact-main .sep { margin: 0 12px; }
  .contact-address { top: 1150px; font-size: 14px; letter-spacing: 2.6px; }
</style>
</head>
<body>
<main class="flyer">
  <div class="stage-scene" role="img" aria-label="Faint photo of a DJ mixing deck under purple club lights"></div>

  <svg class="beams" width="914" height="1200" viewBox="0 0 914 1200" aria-hidden="true">
    <defs>
      <linearGradient id="beamCyan" x1="0" y1="0" x2="1" y2="1">
        <stop offset="0" stop-color="#7ff4ff" stop-opacity="0"/>
        <stop offset=".5" stop-color="#bffaff" stop-opacity=".55"/>
        <stop offset="1" stop-color="#7ff4ff" stop-opacity="0"/>
      </linearGradient>
    </defs>
    <g transform="rotate(45 456 525)">
      <rect x="-200" y="300" width="1300" height="60" fill="url(#beamCyan)"/>
      <rect x="-200" y="390" width="1300" height="26" fill="url(#beamCyan)" opacity=".7"/>
      <rect x="240" y="-300" width="50" height="1300" fill="url(#beamCyan)" opacity=".8"/>
      <rect x="620" y="-300" width="34" height="1300" fill="url(#beamCyan)" opacity=".5"/>
    </g>
    <polygon points="456,160 830,525 456,890 82,525" fill="rgba(120,110,255,.18)"/>
    <polygon points="456,190 800,525 456,860 112,525" fill="none" stroke="rgba(200,220,255,.25)" stroke-width="2"/>
    <polygon points="456,219 786,525 456,831 126,525" fill="var(--diamond-fill)" fill-opacity=".92" stroke="#ffffff" stroke-width="3"/>
    <polygon points="297,395 607,395 600,420 607,446 297,446 304,420" fill="none" stroke="#ffffff" stroke-width="1.5"/>
    <g fill="#bffaff">
      <circle cx="200" cy="280" r="4"/><circle cx="110" cy="320" r="5"/><circle cx="740" cy="570" r="6"/>
      <circle cx="860" cy="680" r="4"/><circle cx="660" cy="850" r="5"/><circle cx="780" cy="230" r="3"/>
    </g>
  </svg>

  <h2 class="headline event-name">VELVET TIDELINE</h2>
  <h1 class="headline event-title">DJ COMPETITION</h1>

  <div class="prizes-label">PRIZES</div>
  <ul class="prize-list">
    <li>Exclusive Interview &amp; Airplay on <span class="station">BLAZE FM</span></li>
    <li>Online Feature Interview on Loopwire Magazine</li>
    <li>Live Gigs</li>
    <li>Mentoring, Recording + Heaps More!</li>
  </ul>
  <div class="school-name"><span class="dot"></span>NORTHGATE ACADEMY OF SOUND</div>

  <div class="presenter"><span class="short">NAS</span><span class="verb">presents</span></div>

  <p class="judges">JUDGES: MARA QUINN<span class="sep">|</span>THEO VANCE<span class="sep">|</span>LENA K</p>

  <div class="cta">AUDITIONS NOW OPEN</div>

  <p class="contact contact-label">BOOK YOUR AUDITION AT:</p>
  <p class="contact contact-main">NORTHGATEACADEMYSOUND.COM.AU<span class="sep">|</span>(03) 9000 4812</p>
  <p class="contact contact-address">STUDIO 12 - NORTHGATE ACADEMY OF SOUND LEVEL 2 HARBOUR RD WESTFIELD</p>
</main>
</body>
</html>
```